Tarn-Lix Solutions Stationary Design

Use logo from prior posted project.
Must be professional.
Company Info:
Tarn-Lix Solutions
P.O. Box274913
Boise, Idaho 83742
C. 208.517.3864
F. 208.629-1507
Tag Line: To be finalized in prior projects but perhaps "We Guide Clients to be Better Prepared, More Organized, and Fully Covered." (Subject to change and Open to Suggestions)

```html
<!DOCTYPE html>
<html lang="en">
<head>
<meta charset="utf-8">
<title>Tarn-Lix Solutions Stationery</title>
<link rel="stylesheet" href="https://fonts.googleapis.com/css2?family=Open+Sans:wght@400;600&family=Roboto+Condensed:ital,wght@0,700;1,700&family=Italianno&display=swap">
<style>
  :root {
    --board: #243352;
    --board-line: #2b3b5c;
    --brand-blue: #1862a6;
    --brand-orange: #e8702a;
    --paper: #ffffff;
    --ink: #2a2a2a;
    --label: #e8702a;
  }
  * { margin: 0; padding: 0; box-sizing: border-box; }
  html, body { width: 927px; height: 1200px; overflow: hidden; }
  body {
    position: relative;
    background-color: var(--board);
    background-image:
      linear-gradient(var(--board-line) 1px, transparent 1px),
      linear-gradient(90deg, var(--board-line) 1px, transparent 1px);
    background-size: 6px 6px;
    font-family: "Open Sans", Arial, sans-serif;
    color: var(--ink);
  }
  .sheet { position: absolute; background: var(--paper); box-shadow: 0 2px 8px rgba(0,0,0,.45); overflow: hidden; }
  .abs { position: absolute; }

  .piece-list { position: absolute; left: 150px; top: 96px; width: 195px; text-align: center;
    font-family: "Roboto Condensed", Arial, sans-serif; font-weight: 700; color: #fff; font-size: 16px; line-height: 29.5px; list-style: none; }

  .brand { display: flex; align-items: center; white-space: nowrap; }
  .brand-dot { border-radius: 50%; background: var(--brand-orange); flex: none; }
  .brand-name { color: var(--brand-blue); font-weight: 400; }
  .tagline { font-family: "Italianno", cursive; color: var(--brand-blue); white-space: nowrap; }
  .contact-strip { font-family: "Roboto Condensed", Arial, sans-serif; font-style: italic; font-weight: 700; color: #fff; white-space: nowrap; }

  /* Letterhead */
  .letterhead { left: 368px; top: 16px; width: 542px; height: 703px; }
  .letterhead .top-band { left: 0; top: 0; width: 100%; height: 40px; background: var(--brand-blue);
    font-family: "Roboto Condensed", Arial, sans-serif; font-weight: 700; color: #fff; font-size: 11px; }
  .letterhead .top-band span { position: absolute; top: 13px; }
  .letterhead .brand { left: 18px; top: 45px; gap: 10px; }
  .letterhead .brand-dot { width: 30px; height: 30px; }
  .letterhead .brand-name { font-size: 20px; }
  .letterhead .tagline { left: 115px; top: 70px; font-size: 16px; }
  .letterhead .contact-tab { right: 0; top: 643px; width: 244px; height: 38px; }
  .letterhead .contact-tab .contact-strip { position: absolute; left: 20px; top: 11px; font-size: 12px; }

  /* Business card */
  .card { left: 75px; top: 241px; width: 264px; height: 150px; }
  .card .address { left: 20px; top: 11px; font-size: 13px; line-height: 17px; }
  .card .brand { left: 12px; top: 72px; gap: 8px; }
  .card .brand-dot { width: 24px; height: 24px; }
  .card .brand-name { font-size: 21px; }
  .card .tagline { left: 24px; top: 100px; font-size: 10.5px; }
  .card .bottom-band { left: 0; top: 116px; width: 203px; height: 34px; background: var(--brand-blue); }
  .card .bottom-band .contact-strip { position: absolute; left: 27px; top: 4px; font-size: 11px; }

  /* Fax */
  .fax { left: 21px; top: 473px; width: 542px; height: 704px; }
  .fax .field { font-size: 8px; color: var(--label); text-transform: uppercase; }
  .fax .from-block { left: 336px; top: 22px; font-size: 11px; line-height: 15px; text-align: right; }
  .fax .from-block .field { position: absolute; left: -35px; top: 1px; }
  .fax .brand { left: 440px; top: 24px; }
  .fax .brand-dot { width: 24px; height: 24px; }
  .fax .fax-brand-name { left: 345px; top: 66px; font-size: 17px; color: var(--brand-blue); white-space: nowrap; }
  .fax .check-band { left: 0; top: 89px; width: 480px; height: 20px; background: var(--brand-blue);
    font-size: 8px; color: #fff; text-transform: uppercase; }
  .fax .check { position: absolute; display: flex; align-items: center; gap: 6px; top: 4px; }
  .fax .check i { display: block; width: 11px; height: 11px; background: #fff; }
  .fax .tagline { left: 26px; top: 668px; font-size: 14px; }
  .fax .footer-band { left: 363px; top: 669px; width: 179px; height: 13px; background: var(--brand-blue); }
  .fax .footer-band .contact-strip { position: absolute; left: 9px; top: 0; font-size: 9px; }

  /* Envelope */
  .envelope { left: 325px; top: 806px; width: 569px; height: 255px; }
  .envelope .top-band { left: 0; top: 0; width: 100%; height: 19px; background: var(--brand-blue); }
  .envelope .brand { left: 44px; top: 27px; gap: 6px; }
  .envelope .brand-dot { width: 34px; height: 34px; }
  .envelope .brand-name { font-size: 18px; }
  .envelope .address { left: 88px; top: 57px; font-size: 11px; line-height: 14px; }
</style>
</head>
<body>

<ul class="piece-list">
  <li>Letterhead</li>
  <li>FAX</li>
  <li>#9-Envelope</li>
  <li>Bz Card - Logo</li>
</ul>

<section class="sheet letterhead" aria-label="Letterhead">
  <div class="abs top-band">
    <span style="left:70px">Tarn-Lix Solutions</span>
    <span style="left:218px">P.O. Box 274913</span>
    <span style="left:372px">Boise, Idaho 83742</span>
  </div>
  <div class="abs brand"><span class="brand-dot"></span><span class="brand-name">Tarn-Lix Solutions</span></div>
  <div class="abs tagline">“We Guide Clients to be Better Prepared, More Organized, and Fully Covered.”</div>
  <div class="abs contact-tab">
    <svg width="244" height="38" viewBox="0 0 244 38"><path d="M4 0 H244 V38 H4 Q10 19 4 0 Z" fill="#1862a6"/></svg>
    <span class="contact-strip">C. 208.517.3864 &nbsp;-&nbsp; F. 208.629-1507</span>
  </div>
</section>

<section class="sheet card" aria-label="Business card">
  <div class="abs address">P.O. Box 274913<br>Boise, Idaho 83742</div>
  <div class="abs brand"><span class="brand-dot"></span><span class="brand-name">Tarn-Lix Solutions</span></div>
  <div class="abs tagline">“We Guide Clients to be Better Prepared, More Organized, and Fully Covered.”</div>
  <div class="abs bottom-band"><span class="contact-strip">C. 208.517.3864 &nbsp;-&nbsp; F. 208.629-1507</span></div>
</section>

<section class="sheet fax" aria-label="Fax cover sheet">
  <div class="abs field" style="left:21px;top:24px">To:</div>
  <div class="abs field" style="left:21px;top:48px">Company:</div>
  <div class="abs field" style="left:21px;top:72px">Re:</div>
  <div class="abs field" style="left:254px;top:48px">Date:</div>
  <div class="abs field" style="left:254px;top:72px">Pages:</div>
  <div class="abs from-block">
    <span class="field">From:</span>
    Tarn-Lix Solutions<br>P.O. Box 274913<br>Boise, Idaho 83742
  </div>
  <div class="abs brand"><span class="brand-dot"></span></div>
  <div class="abs fax-brand-name">Tarn-Lix Solutions</div>
  <div class="abs check-band">
    <span class="check" style="left:42px"><i></i>Urgent</span>
    <span class="check" style="left:109px"><i></i>For Review</span>
    <span class="check" style="left:194px"><i></i>Please Comment</span>
    <span class="check" style="left:305px"><i></i>Please Reply</span>
    <span class="check" style="left:388px"><i></i>Please Recycle</span>
  </div>
  <div class="abs tagline">“We Guide Clients to be Better Prepared, More Organized, and Fully Covered.”</div>
  <div class="abs footer-band"><span class="contact-strip">C. 208.517.3864 &nbsp;-&nbsp; F. 208.629-1507</span></div>
</section>

<section class="sheet envelope" aria-label="Number 9 envelope">
  <div class="abs top-band"></div>
  <div class="abs brand"><span class="brand-dot"></span><span class="brand-name">Tarn-Lix Solutions</span></div>
  <div class="abs address">P.O. Box 274913<br>Boise, Idaho 83742</div>
</section>

</body>
</html>
```